Commercial Construction Interior Fitout company needs Logo and Business Cards

We need a logo and business card design. We specialise in Commercial Ceilings, Partitions, Plastering and Carpentry.

Company name: 7QX Commercial Interiors. Would like a professional looking card more than a fancy look. Gloss front preferably black pattern with Fluro Green and white text.

Will need:

Name
Position
Phone
Fax
Email
Postal Address
Web address
Updates

Thank you so much everyone for your efforts and fantastic designs..   If I didn't respond to everyone personally,  my apologises. 

Again, thanks all

R.M                               

Target Market(s)

Existing & New clients in the Construction Industry

Industry/Entity Type

Business

Requirements
Nice to have
• 7QX to be overlapped or made into some sort of Logo

```html
<!DOCTYPE html>
<html lang="en">
<head>
<meta charset="utf-8">
<title>7QX Commercial Interiors – Logo and Business Cards</title>
<link href="https://fonts.googleapis.com/css2?family=Open+Sans:ital,wght@0,400;0,600;0,700;1,400&display=swap" rel="stylesheet">
<style>
  :root {
    --stage: #e9e7e3;
    --card-black: #141414;
    --card-white: #ffffff;
    --fluro-green: #5cbf3a;
    --ink: #3c3c3c;
    --ink-soft: #555555;
    --black-gloss: #3a3a3a;
    --white: #ffffff;
  }
  * { margin: 0; padding: 0; box-sizing: border-box; }
  html, body { width: 1200px; height: 1100px; overflow: hidden; }
  body { font-family: "Open Sans", Arial, sans-serif; background: var(--stage); position: relative; }

  .card-stage { position: absolute; left: 0; top: 0; width: 1200px; height: 915px; background: var(--stage); }

  .card { position: absolute; top: 310px; width: 500px; height: 286px; box-shadow: 0 6px 18px rgba(0,0,0,.18); }
  .card--front { left: 70px; background: var(--card-black); }
  .card--back { left: 630px; background: var(--card-white); }

  .wordmark { display: flex; align-items: center; gap: 12px; font-weight: 600; white-space: nowrap; }
  .wordmark__square { width: 22px; height: 22px; flex: none; }

  .card--front .wordmark { position: absolute; left: 60px; top: 118px; font-size: 30px; color: var(--black-gloss); }
  .card--front .wordmark__square { background: var(--black-gloss); }

  .card--back .wordmark { position: absolute; left: 36px; top: 36px; font-size: 26px; color: var(--ink); }
  .card--back .wordmark__square { background: var(--fluro-green); }

  .holder { position: absolute; left: 36px; top: 100px; }
  .holder__name { color: var(--fluro-green); font-weight: 700; font-size: 16px; }
  .holder__role { color: var(--ink); font-style: italic; font-size: 12px; }

  .contact-list { position: absolute; left: 250px; top: 150px; list-style: none; font-size: 12px; color: var(--ink); line-height: 19px; }
  .contact-list li { display: flex; align-items: flex-start; gap: 7px; }
  .contact-list .icon { width: 13px; height: 13px; margin-top: 3px; flex: none; }

  .logo-band { position: absolute; left: 0; top: 915px; width: 1200px; height: 185px; display: flex; }
  .logo-band__dark { width: 500px; background: #000; display: flex; align-items: center; justify-content: center; }
  .logo-band__light { flex: 1; background: var(--white); display: flex; align-items: center; justify-content: center; }
  .logo-band .wordmark { font-size: 40px; }
  .logo-band__dark .wordmark { color: var(--white); font-size: 34px; }
  .logo-band__dark .wordmark__square { background: var(--white); }
  .logo-band__light .wordmark { color: var(--ink-soft); }
  .logo-band__light .wordmark__square { background: var(--fluro-green); width: 28px; height: 28px; }
</style>
</head>
<body>
  <section class="card-stage">
    <div class="card card--front">
      <div class="wordmark"><span class="wordmark__square"></span>7QX Commercial Interiors</div>
    </div>

    <div class="card card--back">
      <div class="wordmark"><span class="wordmark__square"></span>7QX Commercial Interiors</div>
      <div class="holder">
        <p class="holder__name">Daniel Reyes</p>
        <p class="holder__role">President</p>
      </div>
      <ul class="contact-list">
        <li><svg class="icon" viewBox="0 0 13 13"><rect width="13" height="13" rx="2" fill="#5cbf3a"/><path d="M4 3h2l.7 2-1.2.8a6 6 0 0 0 1.7 1.7L8 6.3l2 .7v2a1 1 0 0 1-1 1A6 6 0 0 1 3 4a1 1 0 0 1 1-1z" fill="#fff"/></svg>901.555.0142</li>
        <li><svg class="icon" viewBox="0 0 13 13"><rect width="13" height="13" rx="2" fill="#5cbf3a"/><rect x="3" y="5" width="7" height="5" fill="#fff"/><rect x="4.5" y="2.5" width="4" height="3" fill="#fff"/></svg>901.555.0187</li>
        <li><svg class="icon" viewBox="0 0 13 13"><rect width="13" height="13" rx="2" fill="#5cbf3a"/><rect x="2.5" y="4" width="8" height="5.5" fill="#fff"/><path d="M2.5 4l4 3 4-3" stroke="#5cbf3a" fill="none"/></svg>info@7qxinteriors.com.au</li>
        <li><svg class="icon" viewBox="0 0 13 13"><rect width="13" height="13" rx="2" fill="#5cbf3a"/><circle cx="6.5" cy="6.5" r="3.5" fill="none" stroke="#fff"/><path d="M3 6.5h7M6.5 3v7" stroke="#fff"/></svg>www.7qxinteriors.com.au</li>
        <li><svg class="icon" viewBox="0 0 13 13"><rect width="13" height="13" rx="2" fill="#5cbf3a"/><path d="M6.5 2.5a3 3 0 0 1 3 3c0 2-3 5-3 5s-3-3-3-5a3 3 0 0 1 3-3z" fill="#fff"/><circle cx="6.5" cy="5.5" r="1" fill="#5cbf3a"/></svg><span>1480 Harlow Street<br>Oakridge TN 38002</span></li>
      </ul>
    </div>
  </section>

  <section class="logo-band">
    <div class="logo-band__dark">
      <div class="wordmark"><span class="wordmark__square"></span>7QX Commercial Interiors</div>
    </div>
    <div class="logo-band__light">
      <div class="wordmark"><span class="wordmark__square"></span>7QX Commercial Interiors</div>
    </div>
  </section>
</body>
</html>
```